Redo our website for our Robotics company

We sell robotic equipment to the restaurant industry. Our current robot, is a cooking robot that cooks up to 15 lbs of food. We will provide a prior website as well as brand guidelines. We plan on using wordpress and take advantage of wordpress's visual (no code) editor.

Current website - https://kelvatrix88.com/ (please note we are only selling Duffle now and no longer selling Pando+

We want someone to take our existing content and design the website as well as layout our content we provide. Here's a suggested site layout:

✅ KelvaTrix88 Website Wireframe / Site Map
1. Home

Purpose: Introduce Duffle, establish credibility, drive demo requests.

Sections:

Hero Section

Headline: “Meet Duffle — Your New Robotic Chef for High-Volume, Consistent Cooking.”

Sub-headline: Increase throughput. Reduce labor. Deliver perfect food every time.

CTA: Request a Demo + Watch Duffle Cook

Visual: Video loop or hero animation of Duffle in action.

How Duffle Works (3-4 steps)

Step cards: Load Ingredients → Select Recipe → Duffle Cooks → Serve

Icons and short explanations.

Key Benefits

Labor savings

Zero inconsistency

24/7 uptime

Throughput increases (30–50% faster)

Health & safety compliance

Who It’s For

QSR restaurants

Fast casual

Catering/commissaries

Ghost kitchens

Case Studies / Testimonials

Logo bar + quotes

“Duffle helped us reduce cooking times by 40%.”

Video Section

“Watch Duffle cook a full batch from start to finish.”

CTA Section

Big banner: Book a Demo

2. Product: “Meet Duffle”

Purpose: Deep dive into hardware, software, safety, reliability.

Sections:

Overview

What Duffle is

What tasks it automates

Where it fits in a kitchen

Hardware Features

High-temperature cooking chamber

Precision sensors

Automated stirring

Automated dispensing

Safety mechanisms (locking lids, auto-shutoff)

Software & AI

Recipe automation

IoT dashboard

Remote monitoring

Predictive maintenance

Specs Table

Dimensions

Power requirements

Capacity (lbs per batch)

Safety certifications

Gallery

Close-ups, installation photos, process shots

CTA: Request a Demo

3. Solutions

Purpose: Show that Duffle solves real operational problems.

Sub-pages or sections:

For Quick-Service Restaurants

Reduce labor cost

Speed up peak-hour demand

For Catering & Commissaries

Large-batch consistency

Automate repetitive cooking tasks

For High-Growth Chains

Replicable quality across multiple locations

Centralized recipe control

Each solution page includes:

A problem statement

How Duffle solves it

Metrics / KPIs

Relevant testimonial

CTA

4. ROI / Economics

Purpose: Sell the financial story clearly.

Sections:

Savings Calculator

Labor hours saved

Cost savings

Throughput increases

Food waste reduction

Before & After Comparison

Traditional kitchen vs. robotic kitchen

Sample ROI

“Payback in as little as 3–6 months.”

Download Full ROI Report (PDF)

5. Case Studies

Purpose: Social proof + real results.

Structure for each case study:

Customer background

Problem

Implementation

KPIs achieved

Labor savings

Consistency improvements

Cooking speed

Quote + photos/video

6. Pricing

Purpose: Start a commercial conversation.

Include:

Subscription model (monthly / annual)

Hardware leasing or purchase options

Installation + training

Support level

CTA to book a sales call

7. About

Purpose: Build trust.

Sections:

Mission statement

Founding team

Advisors/partners

“Why we built Duffle”

8. Resources

Purpose: SEO + education.

Subpages:

Blog (e.g., “The Future of Automated Kitchens”)

Whitepapers

Technical documentation

Product videos

9. Contact

General inquiry form

Sales contact

Support portal

Careers

```html
<!DOCTYPE html>
<html lang="en">
<head>
<meta charset="utf-8">
<title>KelvaTrix88 — Meet Duffle</title>
<link href="https://fonts.googleapis.com/css2?family=Oswald:wght@600;700&family=Montserrat:wght@500;800&family=Poppins:wght@400;500;600&display=swap" rel="stylesheet">
<style>
:root{
  --orange:#ef4a33;
  --orange-2:#f47d4c;
  --ink:#1b1b1b;
  --muted:#555;
  --cream:#fdf1ea;
  --footer:#1c1c1c;
  --line:#e6e6e6;
}
*{box-sizing:border-box;margin:0;padding:0}
html,body{width:1200px;height:4699px;overflow:hidden;background:#fff}
body{font-family:"Poppins",sans-serif;color:var(--ink);position:relative}
.abs{position:absolute}
.center{left:0;right:0;text-align:center}
.h2{font-family:"Oswald",sans-serif;font-weight:700;font-size:40px;letter-spacing:-.5px;text-transform:uppercase;line-height:1.1}
.h2 em{font-style:normal;color:var(--orange)}
.bar{width:74px;height:4px;background:var(--orange);margin:8px auto 0;border-radius:2px}
.btn{display:inline-flex;align-items:center;justify-content:center;height:48px;padding:0 26px;border-radius:24px;font-family:"Montserrat",sans-serif;font-weight:500;font-size:12px;text-transform:uppercase;letter-spacing:.3px;color:var(--ink);border:2px solid var(--ink);background:#fff;white-space:nowrap}
.btn.fill{background:linear-gradient(90deg,var(--orange),var(--orange-2));border-color:transparent;color:#fff}
.btn-row{display:flex;gap:16px;justify-content:center}

/* nav */
.nav{top:0;left:0;width:1200px;height:86px;background:#fff}
.brand{font-family:"Poppins",sans-serif;font-weight:600;font-size:28px;color:var(--orange)}
.nav .brand{left:140px;top:22px}
.nav-links{left:386px;top:35px;width:552px;display:flex;justify-content:space-between;font-family:"Montserrat",sans-serif;font-weight:500;font-size:10px;letter-spacing:0;text-transform:uppercase;white-space:nowrap}
.nav .btn{left:951px;top:18px;height:46px;width:104px;padding:0}

/* hero */
.hero{top:86px;left:0;width:1200px;height:592px;background:linear-gradient(180deg,#4a4c50,#2b2c2f 60%,#141414)}
.hero-title{top:330px;font-family:"Montserrat",sans-serif;color:#fff;font-size:40px;line-height:46px;text-transform:uppercase;font-weight:500}
.hero-title b{font-weight:800}
.hero-sub{top:470px;color:#fff;font-size:15px}
.hero .btn-row{position:absolute;left:0;right:0;top:512px}
.hero .btn.ghost{background:transparent;color:#fff;border-color:#fff}

/* steps */
.steps-title{top:748px}
.step{width:220px;text-align:center}
.step .disc{width:110px;height:110px;border-radius:50%;background:#fff;box-shadow:0 6px 18px rgba(0,0,0,.12);margin:0 auto;position:relative}
.step .disc .art{position:absolute;inset:28px;border-radius:50%;background:radial-gradient(circle,#f26a45,#2a2a2a)}
.step .num{position:absolute;right:4px;top:-4px;width:28px;height:28px;border-radius:50%;background:var(--orange);color:#fff;font-size:11px;font-weight:600;display:flex;align-items:center;justify-content:center}
.step h3{font-size:17px;font-weight:600;margin-top:26px}
.step p{font-size:12px;line-height:17px;color:#333;margin-top:4px;padding:0 20px}

/* benefits */
.benefits{top:1244px;left:0;width:1200px;height:844px;background:var(--cream)}
.card{background:#fff;border-radius:12px;box-shadow:0 6px 20px rgba(0,0,0,.06);text-align:center}
.bcard{width:283px;height:183px;padding:74px 22px 0}
.bcard h3{font-size:22px;font-weight:500;line-height:24px}
.bcard p{font-size:12px;line-height:22px;color:#333;margin-top:8px}
.bicon{width:73px;height:73px;border-radius:10px;background:linear-gradient(180deg,var(--orange-2),var(--orange));display:flex;align-items:center;justify-content:center}

/* who */
.wcard{width:210px;height:278px;padding:4px}
.wcard .photo{height:140px;border-radius:10px;background:linear-gradient(160deg,#6f6a64,#2d2b29)}
.wcard h3{font-size:17px;font-weight:600;margin-top:18px;line-height:20px}
.wcard p{font-size:12px;line-height:17px;color:#333;margin-top:4px;padding:0 10px}

/* testimonials */
.tcard{background:#fff;border-radius:12px;box-shadow:0 6px 20px rgba(0,0,0,.07);padding:26px 24px;height:292px;text-align:left}
.stars{color:#f6b21b;font-size:14px;letter-spacing:2px}
.quote-mark{position:absolute;right:24px;top:22px;font-family:"Oswald",sans-serif;font-size:80px;line-height:60px;color:var(--orange)}
.tcard .co{font-size:14px;font-weight:500;margin-top:6px}
.tcard .q{font-size:13.5px;line-height:24.5px;color:#333;margin-top:10px}
.tcard .who{font-size:13.5px;font-weight:500;margin-top:16px}
.tcard .mark{font-weight:600;font-size:17px;margin-top:8px;color:var(--ink)}
.dots{top:3146px;display:flex;gap:14px;justify-content:center;align-items:center}
.dots i{width:5px;height:5px;border-radius:50%;background:#bbb;display:block}
.dots i.on{width:14px;height:14px;border:2px solid var(--orange);background:radial-gradient(var(--orange) 35%,transparent 40%)}

/* video */
.video{left:266px;top:3435px;width:662px;height:392px;border-radius:24px;background:linear-gradient(160deg,#8a8c90,#3a3b3e 55%,#1d1d1f);box-shadow:0 18px 30px rgba(0,0,0,.18)}
.play{left:567px;top:3597px;width:66px;height:66px;border-radius:50%;background:#fff;display:flex;align-items:center;justify-content:center}

/* cta */
.cta{top:3940px;left:0;width:1200px;height:332px;background:linear-gradient(180deg,#f57a4a,#ee4a33)}
.cta .h2{color:#fff;font-size:52px}
.cta .btn.ghost{background:transparent;color:#fff;border-color:#fff}

/* footer */
.footer{top:4272px;left:0;width:1200px;height:427px;background:var(--footer);color:#fff}
.footer .brand{color:var(--orange);font-size:30px}
.fhead{font-size:16px;font-weight:600;text-transform:uppercase}
.flist{list-style:none;font-size:13px;line-height:28.5px;margin-top:4px}
.finfo{font-size:12.5px;line-height:19px}
.soc{display:flex;align-items:center;gap:10px;font-size:13px;height:41px}
.soc i{width:28px;height:28px;border-radius:50%;border:1.5px solid #fff;display:block}
.soc i.o{background:var(--orange);border-color:var(--orange)}
.email{left:145px;top:4464px;width:260px;height:34px;background:#fff;border-radius:17px;color:#999;font-size:11px;padding:0 14px;display:flex;align-items:center}
.email b{position:absolute;right:4px;top:4px;width:26px;height:26px;border-radius:50%;background:var(--orange)}
</style>
</head>
<body>

<header class="nav abs">
  <div class="brand abs">KelvaTrix88</div>
  <nav class="nav-links abs"><span>Product</span><span>Solutions</span><span>ROI / Economics</span><span>Case Studies</span><span>Pricing</span><span>About</span><span>Resources</span></nav>
  <a class="btn fill abs">Contact</a>
</header>

<section class="hero abs" role="img" aria-label="Row of Duffle robotic cooking machines in a commercial kitchen">
  <h1 class="hero-title abs center"><b>Meet Duffle — Your New<br>Robotic Chef for</b> High-Volume,<br>Consistent Cooking.</h1>
  <p class="hero-sub abs center">Increase throughp-ut. Reduce labor. Deliver perfect food every time.</p>
  <div class="btn-row"><a class="btn">Request a Demo</a><a class="btn ghost">Watch Duffle Cook</a></div>
</section>

<!-- how it works -->
<div class="abs center steps-title"><h2 class="h2">How Duffle <em>Works</em></h2><div class="bar"></div></div>
<svg class="abs" style="left:0;top:860px" width="1200" height="80" aria-hidden="true">
  <g fill="none" stroke="#bbb" stroke-width="1.5" stroke-dasharray="5 5">
    <path d="M270 45 C320 5 360 15 400 40"/>
    <path d="M520 45 C570 5 610 15 650 40"/>
    <path d="M772 45 C820 5 860 15 900 40"/>
  </g>
</svg>
<div class="step abs" style="left:98px;top:846px"><div class="disc"><div class="art" role="img" aria-label="Ingredients icon"></div><span class="num">01</span></div><h3>Load Ingredients</h3><p>Simply Load Prepped Ingredients Into Duffle's Designated Compartments.</p></div>
<div class="step abs" style="left:350px;top:846px"><div class="disc"><div class="art" role="img" aria-label="Touchscreen recipe icon"></div><span class="num">02</span></div><h3>Select Recipe</h3><p>Choose From Hundreds Of Recipes Via The Intuitive Touch Interface.</p></div>
<div class="step abs" style="left:601px;top:846px"><div class="disc"><div class="art" role="img" aria-label="Robot chef icon"></div><span class="num">03</span></div><h3>Duffle Cooks</h3><p>Duffle Precisely Executes The Recipe With Perfect Timing And Technique.</p></div>
<div class="step abs" style="left:851px;top:846px"><div class="disc"><div class="art" role="img" aria-label="Plated dish icon"></div><span class="num">04</span></div><h3>Serve</h3><p>Consistently Perfect Dishes Ready For Plating And Service.</p></div>
<div class="abs center btn-row" style="top:1105px"><a class="btn fill">Request a Demo</a><a class="btn">Watch Duffle Cook</a></div>

<!-- benefits -->
<section class="benefits abs">
  <div class="abs center" style="top:74px"><h2 class="h2">Key <em>Benefits</em></h2><div class="bar"></div></div>
  <p class="abs center" style="top:142px;font-size:13px">Transform Your Kitchen Operations With Cutting-Edge Automation</p>
</section>
<div class="card bcard abs" style="left:140px;top:1477px"><h3>Labor Savings</h3><p>Reduce Kitchen Staff Dependency By Up To 70% During Peak Hours.</p></div>
<div class="card bcard abs" style="left:458px;top:1477px"><h3>Zero Inconsistency</h3><p>Every Plate Is Identical — No More "Depends On Who's Cooking."</p></div>
<div class="card bcard abs" style="left:777px;top:1477px"><h3>24/7 Uptime</h3><p>Duffle Never Calls In Sick And Works Through Breakfast, Lunch, And Late-Night.</p></div>
<div class="card bcard abs" style="left:140px;top:1729px"><h3>Throughput<br>Increases</h3><p>(30–50% Faster) Cook Multiple Orders In Parallel With Perfect Timing.</p></div>
<div class="card bcard abs" style="left:458px;top:1729px"><h3>Health &amp; Safety<br>Compliance</h3><p>No Human Contact With Food After Loading — Built-In HACCP Logging.</p></div>
<div class="card bcard abs" style="left:777px;top:1729px"><h3>Predictable<br>Costs</h3><p>Fixed Operating Cost Per Meal With No Overtime Or Training Expenses.</p></div>
<div class="bicon abs" style="left:245px;top:1437px"><svg width="40" height="30" viewBox="0 0 40 30" fill="#fff"><circle cx="20" cy="8" r="6"/><circle cx="8" cy="11" r="4.5"/><circle cx="32" cy="11" r="4.5"/><path d="M10 28c0-7 4-12 10-12s10 5 10 12z"/><path d="M0 27c0-5 3-9 8-9 2 0 3 1 3 1-2 2-3 5-3 8zM40 27c0-5-3-9-8-9-2 0-3 1-3 1 2 2 3 5 3 8z"/></svg></div>
<div class="bicon abs" style="left:563px;top:1437px"><svg width="40" height="40" viewBox="0 0 40 40" fill="none" stroke="#fff" stroke-width="3"><circle cx="20" cy="20" r="16"/><circle cx="20" cy="20" r="8"/><path d="M16 16l8 8M24 16l-8 8"/></svg></div>
<div class="bicon abs" style="left:882px;top:1437px"><svg width="40" height="40" viewBox="0 0 40 40" fill="none" stroke="#fff" stroke-width="3"><circle cx="22" cy="20" r="13"/><path d="M22 12v8l6 4M4 16a18 18 0 0 1 6-10"/></svg></div>
<div class="bicon abs" style="left:245px;top:1696px"><svg width="40" height="40" viewBox="0 0 40 40" fill="#fff"><rect x="4" y="26" width="7" height="12"/><rect x="15" y="20" width="7" height="18"/><rect x="26" y="14" width="7" height="24"/><path d="M4 18 16 8l6 5 12-11" stroke="#fff" stroke-width="3" fill="none"/></svg></div>
<div class="bicon abs" style="left:563px;top:1696px"><svg width="40" height="40" viewBox="0 0 40 40" fill="none" stroke="#fff" stroke-width="3"><path d="M20 3l12 5v9c0 8-5 13-12 16-7-3-12-8-12-16V8z"/><path d="M14 17l5 5 8-9"/></svg></div>
<div class="bicon abs" style="left:882px;top:1696px"><svg width="40" height="40" viewBox="0 0 40 40" fill="none" stroke="#fff" stroke-width="3"><rect x="4" y="14" width="32" height="20" rx="3"/><circle cx="20" cy="24" r="5"/><circle cx="20" cy="8" r="5"/></svg></div>
<div class="abs center btn-row" style="top:1957px"><a class="btn fill">Request a Demo</a><a class="btn">Watch Duffle Cook</a></div>

<!-- who -->
<div class="abs center" style="top:2173px"><h2 class="h2">Who It's <em>For</em></h2><div class="bar"></div></div>
<div class="card wcard abs" style="left:140px;top:2267px"><div class="photo" role="img" aria-label="Quick-service restaurant counter"></div><h3>QSR Restaurants</h3><p>Perfect For Fast Food Chains Needing Speed And Consistency.</p></div>
<div class="card wcard abs" style="left:376px;top:2267px"><div class="photo" role="img" aria-label="Fast casual kitchen staff plating food"></div><h3>Fast Casual</h3><p>Ideal For Establishments Balancing Quality With Efficiency.</p></div>
<div class="card wcard abs" style="left:611px;top:2267px"><div class="photo" role="img" aria-label="Large commercial commissary kitchen"></div><h3>Catering/<br>Commissaries</h3><p>Scale Production For Large Events And Multiple Locations.</p></div>
<div class="card wcard abs" style="left:846px;top:2267px"><div class="photo" role="img" aria-label="Chefs cooking in a ghost kitchen"></div><h3>Ghost Kitchens</h3><p>Maximize Output With Minimal Space And Staffing Requirements.</p></div>

<!-- testimonials -->
<div class="abs" style="left:0;top:2632px;width:1200px;height:1px;background:var(--line)"></div>
<div class="abs center" style="top:2707px"><h2 class="h2">Case Studies / <em>Testimonials</em></h2><div class="bar"></div></div>
<div class="tcard abs" style="left:-330px;top:2809px;width:439px"><div class="stars">★★★★★</div><div class="co">BunHaus</div><p class="q">"Duffle Helped Us Reduce Cooking Times By 40% While Maintaining Perfect Quality Across All Our Locations. Our Customers Can't Believe The Consistency!"</p><span class="quote-mark">”</span></div>
<div class="tcard abs" style="left:142px;top:2809px;width:436px"><div class="stars">★★★★★</div><div class="co">BunHaus</div><p class="q">"Duffle Helped Us Reduce Cooking Times By 40% While Maintaining Perfect Quality Across All Our Locations. Our Customers Can't Believe The Consistency! "Duffle Helped Us Reduce Cooking Times By 40% While Maintaining Perfect Quality Across All Our Locations."</p><div class="who">Dara Wells, CEO Of BunHaus</div><div class="mark">BunHaus</div><span class="quote-mark">”</span></div>
<div class="tcard abs" style="left:611px;top:2809px;width:438px"><div class="stars">★★★★★</div><div class="co">BunHaus</div><p class="q">"Consistency Went From Our Biggest Headache To Our Competitive Advantage Overnight"Consistency Went From Our Biggest Headache To Our Competitive Advantage Overnight"Consistency Went From Our Biggest Headache To Our Competitive."</p><div class="who">Teo Marquez Owner, Salsa Lane Ghost Kitchens</div><div style="width:26px;height:26px;border-radius:50%;background:#ccc;margin:8px 0 0 18px"></div><span class="quote-mark">”</span></div>
<div class="tcard abs" style="left:1083px;top:2809px;width:438px"><div class="stars">★★★★★</div><div class="co">BunHaus</div><p class="q">"Consistency Went From Our Biggest Headache To Our Competitive Advantage Overnight"Consistency Went From Our Biggest Headache To Our Competitive."</p><div class="who">Teo Marquez Owner</div></div>
<div class="dots abs center"><i></i><i></i><i class="on"></i><i></i><i></i></div>

<!-- video -->
<div class="abs center" style="top:3296px"><h2 class="h2" style="line-height:44px">Watch Duffle Cook A<br><em>Full Batch From Start To Finish.</em></h2><div class="bar"></div></div>
<div class="video abs" role="img" aria-label="Video preview of Duffle cooking machines in operation"></div>
<div class="play abs"><svg width="22" height="24" viewBox="0 0 22 24"><path d="M3 2l17 10L3 22z" fill="var(--orange)"/></svg></div>

<!-- cta -->
<section class="cta abs">
  <h2 class="h2 abs center" style="top:86px">Ready To Transform Your Kitchen?</h2>
  <p class="abs center" style="top:160px;color:#fff;font-size:14px">Book A Demo Today And See How Duffle Can Revolutionize Your Food Production.</p>
  <div class="abs center btn-row" style="top:210px"><a class="btn">Request a Demo</a><a class="btn ghost">Watch Duffle Cook</a></div>
</section>

<!-- footer -->
<footer class="footer abs">
  <div class="brand abs" style="left:145px;top:78px">KelvaTrix88</div>
  <p class="abs" style="left:145px;top:128px;font-size:12px;line-height:19px;width:290px">Latest Updates, Exclusive Content, And Special Offers? Subscribe To Our Newsletter!</p>
  <div class="abs" style="left:505px;top:82px"><div class="fhead">Quick Links</div><ul class="flist"><li>Home</li><li>Product</li><li>Solutions</li><li>ROI / Economics</li><li>Case Studies</li><li>Pricing</li><li>About</li><li>Resources</li><li>Contact</li></ul></div>
  <div class="abs" style="left:693px;top:82px;width:200px"><div class="fhead">Contact Details</div>
    <div class="finfo" style="margin-top:12px;display:flex;gap:10px"><svg width="14" height="16" viewBox="0 0 14 16"><path d="M7 0a6 6 0 0 1 6 6c0 4-6 10-6 10S1 10 1 6a6 6 0 0 1 6-6z" fill="#fff"/><circle cx="7" cy="6" r="2" fill="#1c1c1c"/></svg><span>482 W Harbor Ave,<br>Lakemont, CA 90210</span></div>
    <div class="finfo" style="margin-top:14px;display:flex;gap:10px"><svg width="14" height="14" viewBox="0 0 14 14"><path d="M3 1l2 3-1.5 1.5a8 8 0 0 0 5 5L10 9l3 2-1.5 2.5C6 13 1 8 .5 2.5z" fill="#fff"/></svg><span>Phone<br>+1 [800] 555 0134</span></div>
    <div class="finfo" style="margin-top:14px;display:flex;gap:10px"><svg width="14" height="12" viewBox="0 0 14 12"><rect width="14" height="11" rx="1" fill="#fff"/><path d="M1 1l6 5 6-5" stroke="#1c1c1c" fill="none"/></svg><span>Email<br>info@kelvatrix88.com</span></div>
  </div>
  <div class="abs" style="left:936px;top:82px"><div class="fhead">Social Media</div>
    <div style="margin-top:12px"><div class="soc"><i class="o"></i>Social Feed</div><div class="soc"><i></i>Video Channel</div><div class="soc"><i></i>Pro Network</div><div class="soc"><i></i>Photo Stream</div></div>
  </div>
  <p class="abs center" style="top:392px;font-size:11.5px">© 2025 KelvaTrix88. All Rights Reserved.</p>
</footer>
<div class="email abs">✉&nbsp; Your Email<b></b></div>

</body>
</html>
```